QUILLDESK - Remote Tech Support Site

We are looking for a new very responsive and simple website for our brand Quilldesk.com - a remote technical support company.

This company supports customers Globally in different countries throughout Eur/ North America / South America / Asia etc (please keep this in mind and integrate into the idea).

Its important to us that the design is very explanatory, the customer should easily be able to figure out that we provide computer support right away ... I like one page responsive type designs as well without a bunch of menu items

Here are some similar sites we like - but still looking for a unique design that fits out brand "quilldesk" - I have upload also some layouts i like (but the designs are not important just the layouts), youll see it includes consumer business etc which is important.

MORVEL.COM - I love how clean it is - nice and white easy to see everything

PIXOLANE247.COM - also nice the layout and responsive one page design makes it easy to use

brightfixhub.com - similar to pixolane design as well - you can get the idea im looking for between the two

You will notice those examples are much different then the attachments I added - again this is more of an idea for possible layouts .. attached is also the logo - could inspire color scheme / blue white black etc

Target Market(s)

Home consumers without computer knowledge , older age 45-65, small medium business ... computer repair - slow computers

Industry/Entity Type

Computer Repair

Logo Text

Quilldesk

Coding

Coded - Design and coding required

Number of Pages Required

1 page

Font styles to use
Sans Serif
Other font styles liked:
• your choice responsive

Colors

Designer to choose colors to be used in the design.

Requirements
Must have
• Clean - responsive - professional design - the name says it all - quilldesk
• CALL TO ACTIONS FOR "Get Help Now!" / "Learn More" etc
Nice to have
• We are looking for a new very responsive and simple website for our brand Quilldesk.com - a remote technical support company.
• This company supports customers Globally in different countries throughout Eur/ North America / South America / Asia etc (please keep this in mind and integrate into the idea).
• Its important to us that the design is very explanatory, the customer should easily be able to figure out that we provide computer support right away ... I like one page responsive type designs as well without a bunch of menu items
• Here are some similar sites we like - but still looking for a unique design that fits out brand "quilldesk" - I have upload also some layouts i like (but the designs are not important just the layouts), youll see it includes consumer business etc which is important.
• MORVEL.COM - I love how clean it is - nice and white easy to see everything
• PIXOLANE247.COM - also nice the layout and responsive one page design makes it easy to use
• brightfixhub.com - similar to pixolane design as well - you can get the idea im looking for between the two
Should not have
• dark, packed page - bad small font -

```html
<!DOCTYPE html>
<html lang="en">
<head>
<meta charset="utf-8">
<title>Quilldesk – Remote Tech Support</title>
<link rel="stylesheet" href="https://fonts.googleapis.com/css2?family=Roboto+Condensed:wght@400;700&family=Roboto:wght@300;400&display=swap">
<style>
  :root {
    --blue: #1a8cf0;
    --blue-dark: #0f74d6;
    --black: #050505;
    --ink: #2b2b2b;
    --grey-text: #777;
    --grey-icon: #e3e3e3;
    --grey-bg: #f1f1f1;
    --white: #fff;
    --red: #c8101e;
  }
  * { margin: 0; padding: 0; box-sizing: border-box; }
  html, body { width: 747px; height: 1200px; overflow: hidden; background: var(--white); }
  body { position: relative; font-family: "Roboto Condensed", "Arial Narrow", sans-serif; color: var(--ink); }

  /* Header */
  .site-header { position: absolute; left: 0; top: 0; width: 747px; height: 56px; background: var(--black); border-bottom: 1px solid var(--blue); }
  .brand { position: absolute; left: 10px; top: 12px; display: flex; align-items: center; gap: 7px; }
  .brand-dot { width: 30px; height: 30px; border-radius: 50%; background: var(--blue); }
  .brand-name { font-family: "Roboto", sans-serif; font-weight: 400; font-size: 26px; color: var(--white); letter-spacing: 0.2px; }
  .main-nav a { position: absolute; top: 23px; font-size: 10px; color: var(--white); text-decoration: none; font-weight: 400; }
  .main-nav a.active { color: var(--blue); }

  /* Hero */
  .hero { position: absolute; left: 0; top: 56px; width: 747px; height: 437px; background: radial-gradient(ellipse at 40% 40%, #6a6a6a 0%, #4a4a4a 45%, #2d2d2d 100%); }
  .hero-arrow { position: absolute; top: 186px; }
  .hero-band { position: absolute; left: 0; top: 357px; width: 747px; height: 80px; background: rgba(30,30,30,0.82); }
  .band-icon { position: absolute; left: 76px; top: 10px; }
  .band-text { position: absolute; left: 160px; top: 25px; font-size: 25px; font-weight: 700; color: var(--white); white-space: nowrap; }
  .band-text span { color: var(--blue); margin-left: 8px; }
  .scroll-down { position: absolute; left: 364px; top: 336px; width: 42px; height: 42px; border-radius: 50%; background: rgba(50,50,50,0.9); }

  /* Contact drop panel */
  .contact-panel { position: absolute; left: 561px; top: 58px; width: 176px; background: var(--blue); box-shadow: 0 2px 4px rgba(0,0,0,0.3); }
  .contact-row { height: 28px; display: flex; align-items: center; justify-content: space-between; padding: 0 7px; font-size: 12px; color: var(--white); border-bottom: 1px solid rgba(255,255,255,0.35); }
  .contact-row:last-child { border-bottom: none; }
  .panel-toggle { position: absolute; left: 715px; top: 174px; width: 19px; height: 13px; background: var(--blue); }

  /* How it works */
  .section-title { position: absolute; font-size: 24px; font-weight: 700; color: var(--blue); text-transform: uppercase; border-bottom: 1px solid #ccc; padding-bottom: 2px; white-space: nowrap; }
  .how-title { left: 290px; top: 537px; width: 160px; text-align: center; }
  .step { position: absolute; top: 626px; width: 188px; text-align: center; }
  .step-icon { width: 72px; height: 72px; border-radius: 50%; background: var(--grey-icon); margin: 0 auto; display: flex; align-items: center; justify-content: center; }
  .step-title { margin-top: 12px; font-size: 18px; line-height: 19px; font-weight: 700; color: var(--ink); }
  .step-title em { font-style: normal; color: var(--blue); display: block; }
  .step-rule { border-top: 1px dashed #bbb; margin: 13px 0 8px; }
  .step-text { font-family: "Roboto", sans-serif; font-weight: 300; font-size: 12.5px; line-height: 19px; color: var(--grey-text); }
  .btn { position: absolute; display: flex; align-items: center; justify-content: center; font-size: 18px; color: var(--white); text-decoration: none; }
  .btn-know { left: 285px; top: 858px; width: 139px; height: 29px; background: var(--blue); }

  /* Membership */
  .member { position: absolute; left: 0; top: 922px; width: 747px; height: 278px; background: var(--grey-bg); }
  .member-photo { position: absolute; left: 0; top: 0; width: 417px; height: 278px; background: linear-gradient(100deg, #bdbdbd 0%, #dcdcdc 55%, #f1f1f1 100%); }
  .member-title { left: 417px; top: 32px; width: 290px; text-align: center; }
  .price-lead { position: absolute; left: 417px; top: 114px; width: 300px; text-align: center; font-size: 24px; font-weight: 400; color: var(--ink); }
  .price { position: absolute; left: 417px; top: 144px; width: 300px; text-align: center; font-size: 33px; font-weight: 700; color: var(--ink); }
  .price small { font-size: 14px; color: var(--red); font-weight: 400; }
  .btn-start { left: 503px; top: 211px; width: 125px; height: 34px; background: #2e2e2e; }
</style>
</head>
<body>
  <header class="site-header">
    <div class="brand"><span class="brand-dot"></span><span class="brand-name">quilldesk</span></div>
    <nav class="main-nav">
      <a class="active" href="#" style="left:406px">HOME</a>
      <a href="#" style="left:463px">ABOUT US</a>
      <a href="#" style="left:537px">SERVICES</a>
      <a href="#" style="left:609px">CONTACT US</a>
      <a href="#" style="left:693px">FAQS</a>
    </nav>
  </header>

  <section class="hero" role="img" aria-label="Chalkboard photo with a hand holding chalk and the hand-written words We focus on quality">
    <svg class="hero-arrow" style="left:28px" width="14" height="40" viewBox="0 0 14 40"><path d="M12 2 L3 20 L12 38" fill="none" stroke="rgba(255,255,255,0.35)" stroke-width="2"/></svg>
    <svg class="hero-arrow" style="left:674px" width="14" height="40" viewBox="0 0 14 40"><path d="M2 2 L11 20 L2 38" fill="none" stroke="rgba(255,255,255,0.35)" stroke-width="2"/></svg>
    <div class="hero-band">
      <svg class="band-icon" width="58" height="60" viewBox="0 0 58 60">
        <circle cx="29" cy="22" r="17" fill="none" stroke="#fff" stroke-width="3"/>
        <path d="M6 58 Q6 40 29 40 Q52 40 52 58 Z" fill="#fff"/>
        <text x="29" y="27" text-anchor="middle" font-family="Roboto Condensed, sans-serif" font-weight="700" font-size="13" fill="#fff">24/7</text>
      </svg>
      <div class="band-text">Dedicated Support<span>Anytime Anywhere</span></div>
    </div>
    <div class="scroll-down">
      <svg width="42" height="42" viewBox="0 0 42 42"><path d="M15 17 L27 17 L21 25 Z" fill="#222"/></svg>
    </div>
  </section>

  <aside class="contact-panel">
    <div class="contact-row">(555) 014-2290
      <svg width="10" height="16" viewBox="0 0 10 16"><rect x="1" y="1" width="8" height="14" rx="1.5" fill="none" stroke="#fff" stroke-width="1.5"/><rect x="3.5" y="12" width="3" height="1.5" fill="#fff"/></svg></div>
    <div class="contact-row">info@quilldesk.com
      <svg width="18" height="12" viewBox="0 0 18 12"><rect x="1" y="1" width="16" height="10" fill="none" stroke="#fff" stroke-width="1.5"/><path d="M1 1 L9 7 L17 1" fill="none" stroke="#fff" stroke-width="1.5"/></svg></div>
    <div class="contact-row">United States - EN
      <svg width="14" height="14" viewBox="0 0 14 14"><circle cx="7" cy="7" r="6" fill="#fff"/><path d="M4 3 Q7 5 5 8 Q8 9 9 12 M9 2 Q10 5 12 6" fill="none" stroke="#1a8cf0" stroke-width="1.4"/></svg></div>
    <div class="contact-row">Login
      <svg width="14" height="16" viewBox="0 0 14 16"><path d="M5 1 H13 V15 H5" fill="none" stroke="#fff" stroke-width="1.5"/><path d="M1 8 H9 M6 5 L9 8 L6 11" fill="none" stroke="#fff" stroke-width="1.5"/></svg></div>
  </aside>
  <div class="panel-toggle"><svg width="19" height="13" viewBox="0 0 19 13"><path d="M5 4 L9.5 8 L14 4" fill="none" stroke="#0a2a55" stroke-width="2"/></svg></div>

  <h2 class="section-title how-title">How it works</h2>

  <div class="step" style="left:60px">
    <div class="step-icon"><svg width="48" height="36" viewBox="0 0 48 36"><path d="M2 20 H12 L17 6 L25 32 L31 20 H43" fill="none" stroke="#1a8cf0" stroke-width="3" stroke-linejoin="round"/><circle cx="44" cy="20" r="3" fill="#1a8cf0"/></svg></div>
    <h3 class="step-title"><em>FREE</em>Diagnostic</h3>
    <div class="step-rule"></div>
    <p class="step-text">Get a diagnostic, FOR FREE! Get a free consultation with our staff.</p>
  </div>

  <div class="step" style="left:271px">
    <div class="step-icon"><svg width="40" height="40" viewBox="0 0 40 40"><path d="M8 18 H14 V35 H8 Z M14 19 L20 6 Q24 5 23 12 L22 17 H32 Q35 18 34 22 L31 33 Q30 35 27 35 H14" fill="#fff" stroke="#222" stroke-width="2" stroke-linejoin="round"/></svg></div>
    <h3 class="step-title"><em>Get</em>Fixed</h3>
    <div class="step-rule"></div>
    <p class="step-text">Get fixed, IMMEDIATELY!<br>Our staff will solve your computer issues right before your eyes.</p>
  </div>

  <div class="step" style="left:502px">
    <div class="step-icon"><svg width="46" height="46" viewBox="0 0 46 46"><g fill="#1a8cf0"><ellipse cx="18" cy="8" rx="14" ry="5"/><path d="M4 12 Q18 19 32 12 V19 Q18 26 4 19 Z"/><path d="M4 23 Q18 30 32 23 V30 Q18 37 4 30 Z"/></g><path d="M36 22 V38 M30 33 L36 40 L42 33" fill="none" stroke="#1a8cf0" stroke-width="4"/></svg></div>
    <h3 class="step-title"><em>Backup your</em>information!</h3>
    <div class="step-rule"></div>
    <p class="step-text">Saving your files is now EASY!<br>You will be able to retain your personal files without any loss of data.</p>
  </div>

  <a class="btn btn-know" href="#">Know More</a>

  <section class="member">
    <div class="member-photo" role="img" aria-label="Black and white photo of two colleagues working together at a laptop"></div>
    <h2 class="section-title member-title">Become a member today!</h2>
    <p class="price-lead">STARTING AT ONLY</p>
    <p class="price">$19.99<small>/MONTH</small></p>
    <a class="btn btn-start" href="#">Get Started</a>
  </section>
</body>
</html>
```